Business Card Design Project for Investment Fund

Orvanel Asset Partners is an emerging wealth management firm based in New Jersey. It offers superior investment returns to high net worth individuals and institutions by finding undervalued assets.
We recently selected a company logo which was inspired by the Tucana constellation. Beta Tucanae is a group of six stars, containing star cluster 47 Tucanae, rated the second brightest object in the sky.
Now we need a business card design. Since we are an investment firm, the design should project a sense of stability, growth and professionalism. The owner is interested in something simple yet striking, which of course is consistent with the logo.
Target Market(s)
Wealthy individuals, probably middle aged or older, in the US
Industry/Entity Type
Investment

```html
<!DOCTYPE html>
<html lang="en">
<head>
<meta charset="utf-8">
<title>Orvanel Asset Partners – Business Card</title>
<link rel="stylesheet" href="https://fonts.googleapis.com/css2?family=Arimo:wght@400;700&display=swap">
<style>
  :root {
    --backdrop: #2b2b2d;
    --card-grey: #c3c3c5;
    --card-white: #ffffff;
    --stripe-grey: #6f7072;
    --stripe-slate: #434e57;
    --stripe-blue: #2b2a86;
    --ink: #111111;
    --ink-soft: #7b7b7b;
    --brand-ink: #3a4650;
    --icon-ink: #555555;
  }
  * { box-sizing: border-box; margin: 0; padding: 0; }
  html, body { width: 1200px; height: 1000px; overflow: hidden; }
  body {
    background: var(--backdrop);
    font-family: "Arimo", Arial, sans-serif;
    position: relative;
  }
  .card {
    position: absolute;
    left: 250px;
    width: 700px;
    height: 400px;
    overflow: hidden;
  }
  .card--front { top: 70px; background: var(--card-grey); }
  .card--back { top: 530px; background: var(--card-white); }

  .stripes { position: absolute; top: 0; bottom: 0; display: flex; }
  .stripes span { display: block; height: 100%; width: 17px; }
  .stripe-grey { background: var(--stripe-grey); }
  .stripe-slate { background: var(--stripe-slate); }
  .stripe-blue { background: var(--stripe-blue); }
  .card--front .stripes { right: 16px; }
  .card--back .stripes { left: 26px; }

  .brand {
    position: absolute;
    left: 0; right: 60px;
    top: 120px;
    display: flex;
    flex-direction: column;
    align-items: center;
    gap: 22px;
  }
  .brand-mark {
    width: 92px; height: 92px;
    border-radius: 12px;
    background: var(--stripe-blue);
  }
  .brand-name {
    font-weight: 700;
    font-size: 30px;
    letter-spacing: 1px;
    color: var(--brand-ink);
  }

  .contact { position: absolute; left: 235px; top: 100px; }
  .contact-name { font-size: 46px; color: var(--ink); font-weight: 400; line-height: 1; }
  .contact-title { font-size: 17px; color: var(--ink-soft); margin-top: 8px; letter-spacing: .3px; }
  .contact-list { list-style: none; margin-top: 26px; }
  .contact-item {
    display: flex; align-items: flex-start; gap: 8px;
    font-size: 18px; color: var(--ink); line-height: 1.1;
    margin-bottom: 12px;
  }
  .contact-item svg { flex: none; width: 26px; height: 26px; }
</style>
</head>
<body>

<section class="card card--front" aria-label="Card front">
  <div class="brand">
    <div class="brand-mark"></div>
    <div class="brand-name">Orvanel Asset Partners</div>
  </div>
  <div class="stripes">
    <span class="stripe-grey"></span><span class="stripe-slate"></span><span class="stripe-blue"></span>
  </div>
</section>

<section class="card card--back" aria-label="Card back">
  <div class="stripes">
    <span class="stripe-blue"></span><span class="stripe-slate"></span><span class="stripe-grey"></span>
  </div>
  <div class="contact">
    <h1 class="contact-name">Daniel Hartwell</h1>
    <p class="contact-title">Chief executive officer (CEO)</p>
    <ul class="contact-list">
      <li class="contact-item">
        <svg viewBox="0 0 26 26" aria-hidden="true"><circle cx="13" cy="13" r="12" fill="none" stroke="var(--icon-ink)" stroke-width="1.5"/><path d="M13 20s-5-5.5-5-9a5 5 0 0 1 10 0c0 3.5-5 9-5 9z" fill="var(--icon-ink)"/><circle cx="13" cy="11" r="2" fill="#fff"/></svg>
        <span>48 Alder Row<br>Newark, NJ 07102</span>
      </li>
      <li class="contact-item">
        <svg viewBox="0 0 26 26" aria-hidden="true"><circle cx="13" cy="13" r="12" fill="none" stroke="var(--icon-ink)" stroke-width="1.5"/><rect x="6.5" y="8.5" width="13" height="9" fill="var(--icon-ink)"/><path d="M6.5 8.5l6.5 5 6.5-5" fill="none" stroke="#fff" stroke-width="1.2"/></svg>
        <span>dhartwell@orvanelasset.com</span>
      </li>
      <li class="contact-item">
        <svg viewBox="0 0 26 26" aria-hidden="true"><circle cx="13" cy="13" r="12" fill="none" stroke="var(--icon-ink)" stroke-width="1.5"/><path d="M9 6.5l2.5 3-1.5 1.8c.8 1.8 2 3 3.7 3.8l1.8-1.5 3 2.5-1.6 2.4c-5-.5-9-4.6-9.5-9.6z" fill="var(--icon-ink)"/></svg>
        <span>973-555-0148</span>
      </li>
      <li class="contact-item">
        <svg viewBox="0 0 26 26" aria-hidden="true"><circle cx="13" cy="13" r="12" fill="none" stroke="var(--icon-ink)" stroke-width="1.5"/><circle cx="13" cy="13" r="8" fill="none" stroke="var(--icon-ink)" stroke-width="1.3"/><ellipse cx="13" cy="13" rx="3.5" ry="8" fill="none" stroke="var(--icon-ink)" stroke-width="1.1"/><path d="M5 13h16" stroke="var(--icon-ink)" stroke-width="1.1"/></svg>
        <span>www.orvanelasset.com</span>
      </li>
    </ul>
  </div>
</section>

</body>
</html>
```